Business Cards for Voslin Maybury, a law firm

We changed our firm's name from "Voslin & Maybury LLP" to "Voslin Maybury", we need to update our cards with a new design. We like the overall look of the back but the front side of the cards (see attached mockup) needs a refreshed look. I also attach our current logo so you can get rid of that LLP and &. We have a new address as well (not same as on mockup).

Target Market(s)

Clients of law firm

Industry/Entity Type

Law Firm

Contact Information for Business Card

Frontsides:

Tommaso L. Voslin
Partner
Tel: (416) 555-0172 ext. 101
Fax: (647) 555-0139
Email: tvoslin@vmlegal.ca

Peter J. Maybury
Partner
Tel: (416) 555-0172 ext. 102
Fax: (647) 555-0139
Email: petermaybury@vmlegal.ca

Reid O. Fanshaw
Barrister
Tel: (416) 555-0172 ext. 104
Fax: (647) 555-0139
Email: rfanshaw@vmlegal.ca

The back side should be crimson red (see mockup) with the logo (please update it to remove the & and the LLP, you can modify it a bit to make it tasteful if need be). Our new address is

218 Harwood Ave W, Suite 307
Toronto, ON M3K 2J5

After our address, please also include our website www.vmlegal.ca

Font styles to use
Sans Serif

Colors
ec2027
ffffff
000000

Requirements
Must have
• PLEASE NOTE: our firm's colour is more of a darker/crimson red, not a vibrant red.
• The front should have space for the lawyer's name, title, phone number (with extension), fax number, and email.
• If you're going to add those yourself, the info for the frontside is in the "Business Card Details" section (three lawyers that need their own cards).
Nice to have
• We like the backside of our current cards, just update it with our new address (one address now instead of 2), and a slightly modified logo (not a new logo altogether).
• The frontside should be refreshed with a better look (think minimalist, professional and modern), although still predominantly white-based background.
Should not have
• No scales of justice or other cheesy lawyer stereotype symbols! :-)

```html
<!DOCTYPE html>
<html lang="en">
<head>
<meta charset="utf-8">
<title>Voslin Maybury – Business Cards</title>
<link rel="stylesheet" href="https://fonts.googleapis.com/css2?family=Montserrat:wght@400;500;700&display=swap">
<style>
  :root {
    --canvas-bg: #f2f2f2;
    --card-dark: #363636;
    --card-light: #ffffff;
    --crimson: #c8202a;
    --ink: #1a1a1a;
    --paper-text: #ffffff;
    --rule-light: #d9d9d9;
    --rule-dark: #333333;
  }
  * { box-sizing: border-box; margin: 0; padding: 0; }
  html, body {
    width: 1200px;
    height: 324px;
    overflow: hidden;
    background: var(--canvas-bg);
    font-family: "Montserrat", sans-serif;
  }
  .canvas {
    position: relative;
    width: 1200px;
    height: 324px;
  }
  .card {
    position: absolute;
    top: 15px;
    width: 586px;
    height: 285px;
    overflow: hidden;
  }

  /* Back side */
  .card--back {
    left: 20px;
    background: var(--card-dark);
    color: var(--paper-text);
  }
  .brand {
    position: absolute;
    left: 0;
    right: 0;
    top: 62px;
    display: flex;
    flex-direction: column;
    align-items: center;
    gap: 22px;
  }
  .brand__dot {
    width: 58px;
    height: 58px;
    border-radius: 50%;
    background: var(--crimson);
  }
  .brand__name {
    font-size: 27px;
    font-weight: 700;
    letter-spacing: 0.2px;
    color: var(--paper-text);
  }
  .card--back .rule {
    position: absolute;
    left: 0;
    right: 0;
    top: 231px;
    height: 1px;
    background: var(--rule-light);
  }
  .address {
    position: absolute;
    left: 24px;
    top: 241px;
    font-size: 10.5px;
    font-weight: 500;
    line-height: 17px;
    font-style: normal;
  }
  .website {
    position: absolute;
    right: 34px;
    top: 250px;
    font-size: 11px;
    font-weight: 500;
  }

  /* Front side */
  .card--front {
    left: 608px;
    width: 588px;
    background: var(--card-light);
    color: var(--ink);
    box-shadow: 0 1px 6px rgba(0,0,0,0.12);
  }
  .front-brand {
    position: absolute;
    right: 36px;
    top: 56px;
    display: flex;
    align-items: center;
    gap: 8px;
  }
  .front-brand__dot {
    width: 14px;
    height: 14px;
    border-radius: 50%;
    background: var(--crimson);
  }
  .front-brand__name {
    font-size: 16px;
    font-weight: 700;
    color: var(--crimson);
  }
  .person {
    position: absolute;
    left: 32px;
    top: 176px;
  }
  .person__name {
    font-size: 13px;
    font-weight: 700;
    color: var(--crimson);
    letter-spacing: 0.3px;
  }
  .person__title {
    font-size: 11px;
    font-weight: 400;
    color: var(--crimson);
    margin-top: 2px;
  }
  .card--front .rule {
    position: absolute;
    left: 0;
    right: 0;
    top: 219px;
    height: 1px;
    background: var(--rule-dark);
  }
  .contact {
    position: absolute;
    top: 246px;
    font-size: 11px;
    line-height: 16px;
  }
  .contact--phones { left: 32px; }
  .contact--email { left: 316px; }
  .contact__label { font-weight: 700; }
</style>
</head>
<body>
<main class="canvas">

  <section class="card card--back" aria-label="Card back">
    <div class="brand">
      <span class="brand__dot" aria-hidden="true"></span>
      <span class="brand__name">Voslin Maybury</span>
    </div>
    <div class="rule"></div>
    <address class="address">
      218 Harwood Ave W, Suite 307<br>
      Toronto, ON M3K 2J5
    </address>
    <div class="website">www.vmlegal.ca</div>
  </section>

  <section class="card card--front" aria-label="Card front">
    <div class="front-brand">
      <span class="front-brand__dot" aria-hidden="true"></span>
      <span class="front-brand__name">Voslin Maybury</span>
    </div>
    <div class="person">
      <div class="person__name">Tommaso L. Voslin</div>
      <div class="person__title">Partner</div>
    </div>
    <div class="rule"></div>
    <div class="contact contact--phones">
      <div><span class="contact__label">Tel:</span> (416) 555-0172 ext. 101</div>
      <div><span class="contact__label">Fax:</span> (647) 555-0139</div>
    </div>
    <div class="contact contact--email">
      <span class="contact__label">Email:</span> tvoslin@vmlegal.ca
    </div>
  </section>

</main>
</body>
</html>
```